We want a business card/punch card for our business. We are including examples of our current business card (we like the front of our business card and not looking to remake it). We need only back side to be designed in form of a punch card (we are including a sample of the punch card we made, but are unsatisfied). For each $180 spend (9 punches) our clients have $20 off.

Colors
886aae

```html
<!DOCTYPE html>
<html lang="en">
<head>
<meta charset="utf-8">
<title>Thank You &amp; Punch Card</title>
<link href="https://fonts.googleapis.com/css2?family=Nothing+You+Could+Do&display=swap" rel="stylesheet">
<style>
  :root {
    --brand-violet: #886aae;
    --deep-violet: #6a3299;
    --band-violet: #5e3192;
    --periwinkle: #5a68b6;
    --night-blue: #3a66a8;
    --sky-blue: #6f95cc;
    --haze-lilac: #b59ad6;
    --stamp-grey: #9098ac;
    --stamp-dot: #7a4aa8;
    --ink-white: #ffffff;
    --url-ink: #5a3aa8;
  }
  * { margin: 0; padding: 0; box-sizing: border-box; }
  html, body {
    width: 1062px; height: 1200px; overflow: hidden;
    background: var(--band-violet);
  }
  .sheet { position: relative; width: 1062px; height: 1200px; }
  .card-art { position: absolute; inset: 0; display: block; }

  .thanks-heading {
    position: absolute; left: 0; top: 185px; width: 1062px;
    text-align: center;
    font-family: "Nothing You Could Do", cursive;
    font-weight: 400; font-size: 104px; line-height: 1;
    color: var(--ink-white); letter-spacing: 2px;
    transform: translateX(-14px);
  }

  .punch-stamp {
    position: absolute; width: 146px; height: 146px; border-radius: 50%;
    background: var(--stamp-grey);
    box-shadow: 0 5px 10px rgba(30, 20, 70, 0.55), inset 0 0 0 2px rgba(255,255,255,0.12);
  }
  .punch-stamp::before {
    content: ""; position: absolute; inset: 8px; border-radius: 50%;
    border: 2px dotted var(--stamp-dot);
  }
  .punch-stamp .stamp-figure {
    position: absolute; left: 50%; top: 50%; width: 70px; height: 86px;
    transform: translate(-50%, -50%); border-radius: 35px;
    background: radial-gradient(ellipse at center, #8a6ab4 0%, var(--stamp-grey) 75%);
    opacity: 0.7;
  }

  .site-address {
    position: absolute; left: 0; top: 880px; width: 1062px; text-align: center;
    font-family: "Nothing You Could Do", cursive;
    font-size: 54px; line-height: 1; color: var(--url-ink); opacity: 0.85;
  }
</style>
</head>
<body>
<main class="sheet">
  <svg class="card-art" width="1062" height="1200" viewBox="0 0 1062 1200" aria-hidden="true">
    <defs>
      <linearGradient id="thanks-sky" x1="0" y1="0" x2="0" y2="1">
        <stop offset="0" stop-color="#3f68aa"/>
        <stop offset="0.6" stop-color="#5d84c2"/>
        <stop offset="1" stop-color="#7b9ad0"/>
      </linearGradient>
      <radialGradient id="thanks-glow" cx="0.45" cy="0.35" r="0.4">
        <stop offset="0" stop-color="#b59ad6" stop-opacity="0.85"/>
        <stop offset="1" stop-color="#b59ad6" stop-opacity="0"/>
      </radialGradient>
      <linearGradient id="punch-sky" x1="0" y1="0" x2="0" y2="1">
        <stop offset="0" stop-color="#2c63b0"/>
        <stop offset="0.5" stop-color="#4a78c0"/>
        <stop offset="1" stop-color="#7aa0d6"/>
      </linearGradient>
    </defs>

    <!-- thank-you panel -->
    <rect x="0" y="0" width="1062" height="590" fill="var(--periwinkle)"/>
    <path d="M0 92 C 260 40, 520 60, 700 40 S 980 10, 1062 18" fill="none" stroke="var(--deep-violet)" stroke-width="8"/>
    <path d="M0 100 C 260 48, 520 68, 700 48 S 980 18, 1062 26 L1062 520 C 900 530, 700 560, 500 566 C 300 572, 100 568, 0 566 Z" fill="url(#thanks-sky)"/>
    <g role="img" aria-label="Faint line illustration of a classical Indian couple behind the greeting">
      <path d="M0 100 C 260 48, 520 68, 700 48 S 980 18, 1062 26 L1062 520 C 900 530, 700 560, 500 566 C 300 572, 100 568, 0 566 Z" fill="url(#thanks-glow)"/>
    </g>
    <path d="M0 566 C 100 568, 300 572, 500 566 C 700 560, 900 530, 1062 505 L1062 590 L0 590 Z" fill="var(--band-violet)"/>
    <path d="M0 566 C 100 568, 300 572, 500 566 C 700 560, 900 530, 1062 505" fill="none" stroke="#4a5cb0" stroke-width="6"/>

    <!-- divider -->
    <rect x="0" y="590" width="1062" height="12" fill="#3b4aa0"/>

    <!-- punch-card panel -->
    <rect x="0" y="602" width="1062" height="598" fill="var(--periwinkle)"/>
    <path d="M0 660 C 250 630, 500 625, 700 640 S 950 640, 1062 615" fill="none" stroke="var(--deep-violet)" stroke-width="7"/>
    <g role="img" aria-label="Starry night sky with faint mandala and figure line drawings">
      <path d="M0 668 C 250 638, 500 633, 700 648 S 950 648, 1062 623 L1062 1090 C 900 1150, 700 1175, 450 1178 C 250 1180, 100 1176, 0 1172 Z" fill="url(#punch-sky)"/>
    </g>
    <path d="M0 1172 C 100 1176, 250 1180, 450 1178 C 700 1175, 900 1150, 1062 1090 L1062 1200 L0 1200 Z" fill="var(--band-violet)"/>
    <path d="M0 1172 C 100 1176, 250 1180, 450 1178 C 700 1175, 900 1150, 1062 1090" fill="none" stroke="#4a5cb0" stroke-width="6"/>
  </svg>

  <h1 class="thanks-heading">Thank you!</h1>

  <section class="punch-row" aria-label="Punch card stamps">
    <div class="punch-stamp" style="left:51px;top:681px"><div class="stamp-figure" role="img" aria-label="Embracing couple silhouette"></div></div>
    <div class="punch-stamp" style="left:261px;top:681px"><div class="stamp-figure" role="img" aria-label="Kneeling couple silhouette"></div></div>
    <div class="punch-stamp" style="left:471px;top:681px"><div class="stamp-figure" role="img" aria-label="Embracing couple silhouette"></div></div>
    <div class="punch-stamp" style="left:681px;top:681px"><div class="stamp-figure" role="img" aria-label="Kneeling couple silhouette"></div></div>
    <div class="punch-stamp" style="left:875px;top:681px"><div class="stamp-figure" role="img" aria-label="Embracing couple silhouette"></div></div>

    <div class="punch-stamp" style="left:51px;top:977px"><div class="stamp-figure" role="img" aria-label="Kneeling couple silhouette"></div></div>
    <div class="punch-stamp" style="left:261px;top:977px"><div class="stamp-figure" role="img" aria-label="Embracing couple silhouette"></div></div>
    <div class="punch-stamp" style="left:471px;top:977px"><div class="stamp-figure" role="img" aria-label="Kneeling couple silhouette"></div></div>
    <div class="punch-stamp" style="left:681px;top:977px"><div class="stamp-figure" role="img" aria-label="Embracing couple silhouette"></div></div>
    <div class="punch-stamp" style="left:875px;top:977px"><div class="stamp-figure" role="img" aria-label="Kneeling couple silhouette"></div></div>
  </section>

  <p class="site-address">lunarpractices.com</p>
</main>
</body>
</html>
```